Accounting business needs a fridge magnet design

I need a business card size design to be used as a fridge magnet.
It will need to be vertical not horizontal and it will have my logo and the services I provide listed below it.
It needs to be pleasing to the eye and catch peoples attention.
I have uploaded my current business card as a reference.
It can look totally different though, i am open to new ideas.

It will need to say:

Specialising in:
*Small Business Taxation
*Company & Trust Returns
*Financial Statements
*Partnership Taxation
*BAS preparation/lodgement
*Capital Gains Tax
*Business Start Ups
*Business Structuring
*Tax Planning

```html
<!DOCTYPE html>
<html lang="en">
<head>
<meta charset="utf-8">
<title>North Tax – Fridge Magnet</title>
<link href="https://fonts.googleapis.com/css2?family=Lato:wght@400;700;900&family=Montserrat:wght@400&display=swap" rel="stylesheet">
<style>
  :root {
    --page: #ffffff;
    --charcoal: #2e2f31;
    --paper: #ffffff;
    --orange: #f7941d;
    --orange-fold: #8a5a12;
    --ink: #2b2b2b;
  }
  html, body {
    margin: 0;
    padding: 0;
    width: 1200px;
    height: 1200px;
    overflow: hidden;
    background: var(--page);
  }
  .magnet {
    position: absolute;
    left: 361px;
    top: 182px;
    width: 478px;
    height: 837px;
    border-radius: 14px;
    background: var(--paper);
    overflow: hidden;
  }
  .side-strip {
    position: absolute;
    top: 0;
    bottom: 0;
    background: var(--charcoal);
  }
  .side-strip--left { left: 0; width: 42px; }
  .side-strip--right { right: 0; width: 37px; }

  .brand {
    position: absolute;
    left: 0;
    right: 0;
    top: 0;
    text-align: center;
  }
  .brand-mark {
    position: absolute;
    left: 193px;
    top: 16px;
    width: 92px;
    height: 92px;
    border: 2px solid var(--ink);
    border-radius: 50%;
    box-sizing: border-box;
  }
  .brand-name {
    position: absolute;
    left: 0;
    right: 0;
    top: 126px;
    margin: 0;
    font-family: "Montserrat", sans-serif;
    font-weight: 400;
    font-size: 31px;
    letter-spacing: 17px;
    padding-left: 17px;
    color: var(--ink);
    line-height: 1;
  }
  .tagline {
    position: absolute;
    left: 0;
    right: 0;
    top: 170px;
    margin: 0;
    font-family: "Lato", sans-serif;
    font-weight: 900;
    font-size: 22px;
    letter-spacing: 1.5px;
    color: var(--ink);
    line-height: 1;
    text-align: center;
  }

  .services {
    list-style: none;
    margin: 0;
    padding: 0;
  }
  .service {
    position: absolute;
    left: 18px;
    width: 447px;
    height: 50px;
    background: var(--orange);
    border-radius: 2px;
    color: #fff;
    font-family: "Lato", sans-serif;
    font-weight: 700;
    font-size: 22.5px;
    letter-spacing: 0.3px;
    line-height: 50px;
    text-align: center;
  }
  .service::before,
  .service::after {
    content: "";
    position: absolute;
    top: 100%;
    width: 0;
    height: 0;
    border-top: 10px solid var(--orange-fold);
  }
  .service::before { left: 0; border-left: 24px solid transparent; }
  .service::after { right: 0; border-right: 24px solid transparent; }

  .contact {
    position: absolute;
    left: 0;
    right: 0;
    top: 780px;
    display: flex;
    justify-content: center;
    align-items: center;
    gap: 16px;
    padding-right: 6px;
  }
  .contact-icon { width: 56px; height: 46px; }
  .contact-number {
    font-family: "Lato", sans-serif;
    font-weight: 900;
    font-size: 41px;
    color: var(--ink);
    letter-spacing: 0.5px;
    line-height: 1;
  }
</style>
</head>
<body>
  <main class="magnet">
    <div class="side-strip side-strip--left"></div>
    <div class="side-strip side-strip--right"></div>

    <header class="brand">
      <span class="brand-mark" aria-hidden="true"></span>
      <h1 class="brand-name">NORTH TAX</h1>
      <p class="tagline">SPECIALISING IN:</p>
    </header>

    <ul class="services">
      <li class="service" style="top:205px">SMALL BUSINESS TAXATION</li>
      <li class="service" style="top:269px">COMPANY &amp; TRUST RETURNS</li>
      <li class="service" style="top:333px">FINANCIAL STATEMENTS</li>
      <li class="service" style="top:397px">PARTNERSHIP TAXATION</li>
      <li class="service" style="top:461px">BAS PREPARATION/LODGEMENT</li>
      <li class="service" style="top:525px">CAPITAL GAINS TAX</li>
      <li class="service" style="top:589px">BUSINESS START UPS</li>
      <li class="service" style="top:653px">BUSINESS STRUCTURING</li>
      <li class="service" style="top:717px">TAX PLANNING</li>
    </ul>

    <div class="contact">
      <svg class="contact-icon" viewBox="0 0 56 46" aria-hidden="true">
        <path d="M4 14 Q28 -2 52 14 L52 20 L42 20 L40 14 Q28 10 16 14 L14 20 L4 20 Z" fill="#2b2b2b"/>
        <path d="M14 18 L42 18 L50 40 Q50 44 46 44 L10 44 Q6 44 6 40 Z" fill="#2b2b2b"/>
        <g fill="#ffffff">
          <circle cx="22" cy="28" r="1.8"/><circle cx="28" cy="28" r="1.8"/><circle cx="34" cy="28" r="1.8"/>
          <circle cx="22" cy="33" r="1.8"/><circle cx="28" cy="33" r="1.8"/><circle cx="34" cy="33" r="1.8"/>
          <circle cx="22" cy="38" r="1.8"/><circle cx="28" cy="38" r="1.8"/><circle cx="34" cy="38" r="1.8"/>
        </g>
      </svg>
      <span class="contact-number">0412 555 019</span>
    </div>
  </main>
</body>
</html>
```